FOOD TRAILER Design Wrap for a Juice Shop (fun/joyful elements)

The business is a sugarcane juice bar.

We require a design for the front and back of the trailer. (we have attached a quick mock-up we created ourselves along with some of our bus advertisement designs for a little bit of direction and insporation).

WE ARE LOOKING FOR QUALITY. WE ALREADY HAVE CONCEPTS (AS SHOWN IN ATTACHMENTS) - WE ARE LOOKING FOR SOMETHING MORE CREATIVE AND EYE-CATCHING THAN THIS.

The two white portrait TV looking things on the left and right side of the trailer is where the menus are going to be placed. So please take this into consideration when designing this.

Our motto/slogan is “REAL FRUIT, REAL FLAVOURS.”

Our font is AMERICAN CAPTAIN and is also attached.

Our logo is being built in big 3D Block Light Up letters and will be on top of the trailer so no need to add the logo on the front of the trailer design. ( as shown in our mockup photo)

The logo can go on the back of the trailer design. The back should include the logo, some sort of cool design, our website www.pulpmirra.com.au and our social media following @PULPMIRRA.AU along with the social media icons LUMO, VIBE, Tik Tok & ZEST.

I have attached images of the trailer without any sort of design on it for you to use while designing.

The main background base colour should be our signature green. The colour code for this is #87d500

Our secondary darker green colour code is #248801

To look at our branding please follow these links:

Website – www.pulpmirra.com.au

LUMO – www.instagram.com/pulpmirra.au

VIBE – www.facebook.com/pulpmirra.au

We have our fruit characters being designed at the moment and we should have them in the next 7 or so days that could possibly work really well on the back of the trailer where the website etc. is going however, do not wait for this, feel free to design what you think works for the mean time.

HERE ARE THE DIMENSIONS OF THE TRAILER:

FRONT / BACK
- 4000mm wide (side to side)
- 2140mm height (top to bottom)

- 3850mm wide (vinyl wrap - the actual design)
- 1800 height (vinyl wrap - the actual design)

SIDES
- 1970mm width (vinyl wrap - the actual design)
- 1800 (vinyl wrap - the actual design)

ROOF (be creative with this one, people may be able to see the trailer from a high point)
- 4000mm width
- 2120mm height

Target Market(s)

Healthy people who like fruit juice as alternatives to soft drink

Font styles to use
Other font styles liked:
• AMERICAN CAPTAIN (provided)

Requirements
Must have
• PLEASE READ THE BRIEF!!!! Too many mistakes so far.

Try have each side of the trailer be different from the other. We don't want every single side to look the same..

You can include the juice cups at the back of the trailer but for the front It's probably best to stick to fruit and splashes

Original Design Ideas

Must stand out in any situation/setting where it is parked

Must catch the customers eye

Fruits / collage

splashes with vibrant colours to compliment the fruits

Our Branding colours as main base colours etc

Other colours to compliment (such as the fruits and splashes)

fruits you can include:

- Strawberry
- Watermelon
- Passionfruit
- Pomegranate
- Lemon
- Mango
- Pineapple
- Orange
Nice to have
• Fruits & splashes

```html
<!DOCTYPE html>
<html lang="en">
<head>
<meta charset="utf-8">
<title>Pulpmirra – Trailer Front Wrap</title>
<link rel="stylesheet" href="https://fonts.googleapis.com/css2?family=Bebas+Neue&display=swap">
<style>
  :root{
    --brand-green:#87d500;
    --wrap-green:#80d400;
    --deep-green:#248801;
    --outline-green:#2d5a12;
    --sun-yellow:#fff04a;
    --cream:#fffce6;
    --frame-silver:#cfd4d8;
    --frame-shadow:#9aa1a7;
    --screen-black:#151515;
    --menu-orange:#f0a21a;
    --page:#ffffff;
  }
  *{margin:0;padding:0;box-sizing:border-box}
  html,body{width:1200px;height:1020px;overflow:hidden;background:var(--page)}
  .canvas{display:block;width:1200px;height:1020px}
  .brand-sign{font-family:"Bebas Neue",sans-serif;fill:var(--deep-green)}
  .wrap-type{font-family:"Bebas Neue",sans-serif;paint-order:stroke;stroke:var(--outline-green);stroke-linejoin:round}
  .social-name{font-family:"Bebas Neue",sans-serif;font-size:15px;fill:var(--outline-green)}
  .menu-title{font-family:"Bebas Neue",sans-serif;font-size:16px;fill:var(--deep-green)}
  .menu-title--orange{fill:var(--menu-orange)}
  .menu-note{font-family:"Bebas Neue",sans-serif;font-size:6px;fill:var(--brand-green)}
</style>
</head>
<body>
<svg class="canvas" width="1200" height="1020" viewBox="0 0 1200 1020" xmlns="http://www.w3.org/2000/svg">
  <defs>
    <linearGradient id="type-fill" x1="0" y1="0" x2="0" y2="1">
      <stop offset="0" stop-color="var(--cream)"/>
      <stop offset="1" stop-color="var(--sun-yellow)"/>
    </linearGradient>
    <radialGradient id="soft-red"><stop offset="0" stop-color="#c81e2e"/><stop offset=".65" stop-color="#8c0c18" stop-opacity=".9"/><stop offset="1" stop-color="#8c0c18" stop-opacity="0"/></radialGradient>
    <radialGradient id="soft-yellow"><stop offset="0" stop-color="#ffe24a"/><stop offset=".65" stop-color="#f5b41a" stop-opacity=".85"/><stop offset="1" stop-color="#f5b41a" stop-opacity="0"/></radialGradient>
    <radialGradient id="soft-orange"><stop offset="0" stop-color="#ffc060"/><stop offset=".65" stop-color="#f07a12" stop-opacity=".9"/><stop offset="1" stop-color="#f07a12" stop-opacity="0"/></radialGradient>
    <radialGradient id="soft-lime"><stop offset="0" stop-color="#c4ee7a"/><stop offset=".65" stop-color="#5aa51a" stop-opacity=".85"/><stop offset="1" stop-color="#5aa51a" stop-opacity="0"/></radialGradient>
    <radialGradient id="soft-pink"><stop offset="0" stop-color="#ff8a7a"/><stop offset=".65" stop-color="#d83a44" stop-opacity=".85"/><stop offset="1" stop-color="#d83a44" stop-opacity="0"/></radialGradient>
    <radialGradient id="soft-banana"><stop offset="0" stop-color="#fff7cc"/><stop offset=".65" stop-color="#f3d23a" stop-opacity=".85"/><stop offset="1" stop-color="#f3d23a" stop-opacity="0"/></radialGradient>
    <linearGradient id="cup-red" x1="0" y1="0" x2="0" y2="1"><stop offset="0" stop-color="#c0392b"/><stop offset="1" stop-color="#6e1010"/></linearGradient>
    <linearGradient id="cup-orange" x1="0" y1="0" x2="0" y2="1"><stop offset="0" stop-color="#ffc34a"/><stop offset="1" stop-color="#e67e12"/></linearGradient>
    <clipPath id="wrap-clip"><rect width="1036" height="481"/></clipPath>
    <clipPath id="window-clip"><rect x="196" y="74" width="647" height="212"/></clipPath>
  </defs>

  <text class="brand-sign" x="592" y="280" text-anchor="middle" font-size="200" textLength="706" lengthAdjust="spacingAndGlyphs">PULPMIRRA</text>

  <g class="front-wrap" transform="translate(80 311)">
    <g clip-path="url(#wrap-clip)">
      <rect class="wrap-base" width="1036" height="481" fill="var(--wrap-green)"/>

      <g role="img" aria-label="Mandarin segment, red juice splashes, halved apple and sliced strawberry along the top edge">
        <ellipse cx="72" cy="40" rx="52" ry="40" fill="url(#soft-orange)"/>
        <ellipse cx="270" cy="30" rx="150" ry="50" fill="url(#soft-red)"/>
        <ellipse cx="570" cy="28" rx="70" ry="40" fill="url(#soft-pink)"/>
        <ellipse cx="880" cy="50" rx="190" ry="60" fill="url(#soft-red)"/>
        <ellipse cx="860" cy="20" rx="50" ry="30" fill="url(#soft-pink)"/>
      </g>

      <g role="img" aria-label="Pineapple, orange half, grapefruit and peeled banana with yellow and red juice splashes along the bottom">
        <ellipse cx="500" cy="440" rx="520" ry="90" fill="url(#soft-yellow)"/>
        <ellipse cx="75" cy="390" rx="80" ry="120" fill="url(#soft-yellow)"/>
        <ellipse cx="395" cy="335" rx="90" ry="45" fill="url(#soft-orange)"/>
        <ellipse cx="655" cy="360" rx="80" ry="70" fill="url(#soft-pink)"/>
        <ellipse cx="640" cy="450" rx="130" ry="45" fill="url(#soft-red)"/>
        <ellipse cx="955" cy="390" rx="95" ry="130" fill="url(#soft-banana)"/>
      </g>

      <g class="menu-screen menu-screen--left" transform="translate(19 69)">
        <rect width="138" height="232" fill="var(--screen-black)"/>
        <rect x="5" y="5" width="128" height="222" fill="var(--page)"/>
        <g transform="translate(16 36)"><text class="menu-title">RUBY TWIST</text><text class="menu-note" y="9">Cane, berry &amp; lime</text><rect x="82" y="-17" width="15" height="27" rx="3" fill="url(#cup-red)"/></g>
        <g transform="translate(16 74)"><rect x="6" y="-17" width="15" height="27" rx="3" fill="url(#cup-orange)"/><text class="menu-title menu-title--orange" x="34">SUNNY CITRUS</text><text class="menu-note" x="44" y="9">Cane, orange &amp; mint</text></g>
        <g transform="translate(16 112)"><text class="menu-title">RUBY TWIST</text><text class="menu-note" y="9">Cane, berry &amp; lime</text><rect x="82" y="-17" width="15" height="27" rx="3" fill="url(#cup-red)"/></g>
        <g transform="translate(16 150)"><rect x="6" y="-17" width="15" height="27" rx="3" fill="url(#cup-orange)"/><text class="menu-title menu-title--orange" x="34">SUNNY CITRUS</text><text class="menu-note" x="44" y="9">Cane, orange &amp; mint</text></g>
        <g transform="translate(16 188)"><text class="menu-title">RUBY TWIST</text><text class="menu-note" y="9">Cane, berry &amp; lime</text><rect x="82" y="-17" width="15" height="27" rx="3" fill="url(#cup-red)"/></g>
      </g>

      <g class="menu-screen menu-screen--right" transform="translate(878 69)">
        <rect width="138" height="232" fill="var(--screen-black)"/>
        <rect x="5" y="5" width="128" height="222" fill="var(--page)"/>
        <g transform="translate(16 36)"><text class="menu-title">RUBY TWIST</text><text class="menu-note" y="9">Cane, berry &amp; lime</text><rect x="82" y="-17" width="15" height="27" rx="3" fill="url(#cup-red)"/></g>
        <g transform="translate(16 74)"><rect x="6" y="-17" width="15" height="27" rx="3" fill="url(#cup-orange)"/><text class="menu-title menu-title--orange" x="34">SUNNY CITRUS</text><text class="menu-note" x="44" y="9">Cane, orange &amp; mint</text></g>
        <g transform="translate(16 112)"><text class="menu-title">RUBY TWIST</text><text class="menu-note" y="9">Cane, berry &amp; lime</text><rect x="82" y="-17" width="15" height="27" rx="3" fill="url(#cup-red)"/></g>
        <g transform="translate(16 150)"><rect x="6" y="-17" width="15" height="27" rx="3" fill="url(#cup-orange)"/><text class="menu-title menu-title--orange" x="34">SUNNY CITRUS</text><text class="menu-note" x="44" y="9">Cane, orange &amp; mint</text></g>
        <g transform="translate(16 188)"><text class="menu-title">RUBY TWIST</text><text class="menu-note" y="9">Cane, berry &amp; lime</text><rect x="82" y="-17" width="15" height="27" rx="3" fill="url(#cup-red)"/></g>
      </g>

      <g class="service-window">
        <rect x="174" y="52" width="691" height="258" fill="var(--frame-silver)" stroke="var(--frame-shadow)" stroke-width="2"/>
        <rect x="192" y="70" width="655" height="220" fill="var(--frame-shadow)"/>
        <rect x="196" y="74" width="647" height="212" fill="var(--wrap-green)"/>
        <g clip-path="url(#window-clip)" role="img" aria-label="Pineapple chunk, cherry, leaves, limes and red and green juice splashes">
          <ellipse cx="280" cy="230" rx="110" ry="90" fill="url(#soft-red)"/>
          <ellipse cx="660" cy="80" rx="240" ry="55" fill="url(#soft-red)"/>
          <ellipse cx="250" cy="120" rx="50" ry="42" fill="url(#soft-yellow)"/>
          <ellipse cx="300" cy="185" rx="38" ry="36" fill="url(#soft-red)"/>
          <ellipse cx="780" cy="160" rx="70" ry="62" fill="url(#soft-lime)"/>
          <ellipse cx="740" cy="255" rx="110" ry="45" fill="url(#soft-lime)"/>
        </g>
        <text class="wrap-type" x="397" y="146" font-size="62" textLength="275" lengthAdjust="spacingAndGlyphs" fill="url(#type-fill)" stroke-width="4">WHERE TO NEXT?</text>
        <text class="wrap-type" x="333" y="198" font-size="62" textLength="198" lengthAdjust="spacingAndGlyphs" fill="url(#type-fill)" stroke-width="4">FIND OUT ON</text>
        <g class="social-links">
          <rect x="544" y="152" width="45" height="45" rx="9" fill="url(#type-fill)" stroke="var(--outline-green)" stroke-width="3"/>
          <text class="social-name" x="566.5" y="180" text-anchor="middle">LUMO</text>
          <rect x="596" y="152" width="45" height="45" rx="9" fill="url(#type-fill)" stroke="var(--outline-green)" stroke-width="3"/>
          <text class="social-name" x="618.5" y="180" text-anchor="middle">VIBE</text>
          <rect x="648" y="152" width="45" height="45" rx="9" fill="url(#type-fill)" stroke="var(--outline-green)" stroke-width="3"/>
          <text class="social-name" x="670.5" y="180" text-anchor="middle">KLIP</text>
          <rect x="700" y="152" width="45" height="45" rx="9" fill="url(#type-fill)" stroke="var(--outline-green)" stroke-width="3"/>
          <text class="social-name" x="722.5" y="180" text-anchor="middle">ZEST</text>
        </g>
        <text class="wrap-type" x="371" y="264" font-size="74" textLength="327" lengthAdjust="spacingAndGlyphs" fill="url(#type-fill)" stroke-width="5">@PULPMIRRA.AU</text>
      </g>

      <text class="wrap-type slogan" x="160" y="434" font-size="90" textLength="717" lengthAdjust="spacingAndGlyphs" fill="url(#type-fill)" stroke-width="6">REAL FRUIT, REAL FLAVOURS.</text>
    </g>
  </g>
</svg>
</body>
</html>
```